Introducing a Personal Care Product called" VELO"

We are a nutra-pharmaceutical company launching a new personal care product called VELO. Some of the products include massage and aroma therapy, as well as personal lubricants. The products will be produced and put into, two bottles that are interlocking so two combinations of products can be purchased at once (i.e. massage and aroma therapy). The poster will be used for promotional advertising, trade shows and for in-store promotions.
Updates

We would like to see a design without the product.

Target Market(s)

Products will be aimed at adults primarily women 18-65 in the USA. We want to appeal to the everyday woman who is interested in their sexual well being.

Industry/Entity Type

Massage

Requirements
Must have
• Clean Presentation. Not many colors. Text should be as follows: VELO for Her....VELO for Him...VELO for You...Let's VELO see attached..Also VELO with Her...Velo with Him..Let's VELO..Open to other copy versions.
Nice to have
• Product image not necessary but can be used. image attached
Should not have
• Too many colors...

```html
<!DOCTYPE html>
<html lang="en">
<head>
<meta charset="utf-8">
<title>VELO — Poster</title>
<link rel="stylesheet" href="https://fonts.googleapis.com/css2?family=Cinzel:wght@700&family=Italianno&display=swap">
<style>
  :root {
    --cream: #fbf6cf;
    --cream-edge: #fffef4;
    --blush: #f4ddd6;
    --rose: #e9bfb4;
    --lilac-1: #a98bc8;
    --lilac-2: #8b68ae;
    --lilac-3: #623b8b;
    --lilac-4: #48186a;
    --cap-red: #b3121a;
    --cap-blue: #1f3fb8;
    --clear: #e8ecee;
    --label-pink: #f2b3c2;
    --label-blue: #9fd2ee;
    --skin: #e6bf9f;
  }
  * { box-sizing: border-box; margin: 0; padding: 0; }
  html, body { width: 900px; height: 1200px; overflow: hidden; }
  body { background: var(--cream-edge); }

  .poster {
    position: relative;
    width: 900px;
    height: 1200px;
    overflow: hidden;
    background:
      radial-gradient(ellipse 75% 50% at 55% 35%, var(--cream) 0%, #fcf8df 55%, var(--cream-edge) 100%);
  }

  .floral-band {
    position: absolute;
    left: 0; top: 620px;
    width: 900px; height: 580px;
  }

  .tagline {
    position: absolute;
    left: 0; width: 900px;
    text-align: center;
    white-space: nowrap;
    line-height: 1;
  }
  .tagline .brand {
    font-family: "Cinzel", "Times New Roman", serif;
    font-weight: 700;
    letter-spacing: 1px;
  }
  .tagline .script {
    font-family: "Italianno", cursive;
    margin-left: 12px;
  }
  .tagline--her { top: 92px; color: var(--lilac-1); padding-left: 20px; }
  .tagline--her .brand { font-size: 68px; }
  .tagline--her .script { font-size: 74px; }
  .tagline--him { top: 226px; color: var(--lilac-2); padding-left: 10px; }
  .tagline--him .brand { font-size: 66px; }
  .tagline--him .script { font-size: 72px; }
  .tagline--you { top: 368px; color: var(--lilac-3); padding-left: 18px; }
  .tagline--you .brand { font-size: 58px; }
  .tagline--you .script { font-size: 66px; }
  .tagline--lets { top: 472px; color: var(--lilac-4); padding-left: 10px; }
  .tagline--lets .brand { font-size: 58px; }
  .tagline--lets .script { font-size: 66px; margin-left: 0; margin-right: 8px; }

  .product-pair {
    position: absolute;
    left: 268px; top: 545px;
    width: 376px; height: 492px;
  }

  .spa-scene {
    position: absolute;
    top: 835px;
    width: 250px; height: 200px;
  }
  .spa-scene--left { left: 0; }
  .spa-scene--right { left: 650px; }
</style>
</head>
<body>
  <main class="poster">
    <svg class="floral-band" viewBox="0 0 900 580" role="img" aria-label="Soft floral swirl decoration with a large daisy in blush and peach tones">
      <defs>
        <linearGradient id="band-fade" x1="0" y1="0" x2="0" y2="1">
          <stop offset="0" stop-color="#fbf7d6" stop-opacity="0"/>
          <stop offset="0.35" stop-color="#f8ebdc" stop-opacity="0.7"/>
          <stop offset="0.75" stop-color="#f1d4cb"/>
          <stop offset="1" stop-color="#ecc6bd"/>
        </linearGradient>
        <radialGradient id="band-glow" cx="0.4" cy="0.78" r="0.45">
          <stop offset="0" stop-color="#f6d9c4" stop-opacity="0.9"/>
          <stop offset="1" stop-color="#f6d9c4" stop-opacity="0"/>
        </radialGradient>
      </defs>
      <rect width="900" height="580" fill="url(#band-fade)"/>
      <rect width="900" height="580" fill="url(#band-glow)"/>
    </svg>

    <p class="tagline tagline--her"><span class="brand">VELO</span><span class="script">for her</span></p>
    <p class="tagline tagline--him"><span class="brand">VELO</span><span class="script">for him</span></p>
    <p class="tagline tagline--you"><span class="brand">VELO</span><span class="script">for you</span></p>
    <p class="tagline tagline--lets"><span class="script">Let's</span><span class="brand">VELO</span></p>

    <svg class="spa-scene spa-scene--left" viewBox="0 0 250 200" role="img" aria-label="Photograph of a woman relaxing during a back massage">
      <defs>
        <radialGradient id="spa-left" cx="0.45" cy="0.55" r="0.6">
          <stop offset="0" stop-color="#e3b796"/>
          <stop offset="0.6" stop-color="#eed2bd" stop-opacity="0.8"/>
          <stop offset="1" stop-color="#f6e6dc" stop-opacity="0"/>
        </radialGradient>
      </defs>
      <ellipse cx="115" cy="105" rx="140" ry="100" fill="url(#spa-left)"/>
    </svg>

    <svg class="spa-scene spa-scene--right" viewBox="0 0 250 200" role="img" aria-label="Photograph of a woman relaxing during a back massage">
      <defs>
        <radialGradient id="spa-right" cx="0.55" cy="0.55" r="0.6">
          <stop offset="0" stop-color="#e3b796"/>
          <stop offset="0.6" stop-color="#eed2bd" stop-opacity="0.8"/>
          <stop offset="1" stop-color="#f6e6dc" stop-opacity="0"/>
        </radialGradient>
      </defs>
      <ellipse cx="135" cy="105" rx="140" ry="100" fill="url(#spa-right)"/>
    </svg>

    <svg class="product-pair" viewBox="0 0 376 492" role="img" aria-label="Two interlocking product bottles: a pink warming lubricant for her with a red cap and a blue cooling lubricant for him with a blue cap">
      <defs>
        <linearGradient id="clear-body" x1="0" y1="0" x2="1" y2="0">
          <stop offset="0" stop-color="#dfe4e7"/>
          <stop offset="0.5" stop-color="#f4f6f7"/>
          <stop offset="1" stop-color="#dfe4e7"/>
        </linearGradient>
        <radialGradient id="label-her" cx="0.5" cy="0.5" r="0.6">
          <stop offset="0" stop-color="#f7c9d2"/>
          <stop offset="1" stop-color="#c96a7e"/>
        </radialGradient>
        <radialGradient id="label-him" cx="0.5" cy="0.5" r="0.6">
          <stop offset="0" stop-color="#bfe3f5"/>
          <stop offset="1" stop-color="#4f8fd2"/>
        </radialGradient>
      </defs>
      <rect x="50" y="3" width="115" height="108" rx="8" fill="var(--cap-red)"/>
      <rect x="215" y="3" width="115" height="108" rx="8" fill="var(--cap-blue)"/>
      <rect x="4" y="108" width="186" height="380" rx="18" fill="url(#clear-body)"/>
      <rect x="192" y="108" width="180" height="380" rx="18" fill="url(#clear-body)"/>
      <rect x="17" y="168" width="160" height="278" rx="10" fill="url(#label-her)"/>
      <rect x="222" y="168" width="142" height="278" rx="10" fill="url(#label-him)"/>
    </svg>
  </main>
</body>
</html>
```